Beauty Page

**UPDATED Brief**
We are looking for a website for a beauty organisation that targets both MEN & WOMAN. The focus of the company is in four main areas:

- Health
* Naturopathy & Remedial Massage
- Body
* Yoga
* Personal Training
* Massage
- Skin
* Skin care products such as Velmoracine
- Beauty
* Waxing
* Eye Treatments

We have attached the logo, (a sample of the website that I did - based on the book) and the sample of the pdf book
Updates

Dear All,

Thank you for your patience regarding the beauty contest. We were not happy with the designs that were submitted to us. We therefore had the Graphic designer to do the pricelist book to get all the colours for the organisation.

We are now happy to relaunch the contest and invite you all to take a look at the brief, download a sample of the book and the website we designed on what I’m looking for (the website is only a draft so I don’t want you to copy it) and let your creative mind go wild and present some suggestions to us.

Thanks

 

Target Market(s)

Woman & Men age 24 - 60

Industry/Entity Type

It Company

Requirements
Must have
• Use of main colours
Black
White
Gray - (CYMK - 65, 58, 57, 37)
Purpleish - Maroon (CYMK - 52, 69, 47, 25)

Use of the three color dots on the page.
(white, maroon & Gray)
Same fonts as the book
- Helvetica LT Std
Should not have
• Logo must not be altered i.e different colours, fonts, shadows etc...

```html
<!DOCTYPE html>
<html lang="en">
<head>
<meta charset="utf-8">
<title>Corvelle &amp; Beauty</title>
<link href="https://fonts.googleapis.com/css2?family=Open+Sans:wght@300;400;600;700&family=PT+Sans:ital,wght@0,700;1,400;1,700&display=swap" rel="stylesheet">
<style>
:root{
  --purple:#a020e8;
  --purple-dark:#6f1a9a;
  --purple-deep:#4d1470;
  --violet-soft:#c77ff0;
  --ink:#1b1b1b;
  --grey:#8a8a8a;
  --grey-pill:#a6a6a6;
  --panel:#ececec;
  --white:#ffffff;
  --footer:#2a2a2a;
  --link:#5a1f7a;
  --red:#c0141c;
}
*{box-sizing:border-box;margin:0;padding:0}
html,body{width:1200px;height:1198px;overflow:hidden}
body{position:relative;font-family:"Open Sans",Arial,sans-serif;color:var(--ink);
  background:linear-gradient(180deg,#b12cf0 0,#9c22db 480px,#7d1cb4 760px,#6a1a98 1050px,var(--footer) 1050px)}
.abs{position:absolute}
.topbar .pill{position:absolute;top:0;height:34px;border-radius:0 0 17px 17px;background:var(--grey-pill);
  color:#222;font-size:17px;font-weight:300;line-height:34px;text-align:center}
.cart{left:488px;width:298px}
.checkout{left:797px;width:146px}
.account{left:948px;width:142px;background:linear-gradient(180deg,#e42a2a,#a10c12)!important;color:#fff!important;
  font-family:"PT Sans",sans-serif;font-style:italic;font-weight:700;border:1px solid #fff}
.account .arrow{position:absolute;right:8px;top:8px;width:18px;height:18px;border-radius:50%;background:#fff}
.account .arrow:after{content:"";position:absolute;left:4px;top:6px;border:5px solid transparent;border-top:7px solid var(--red)}
.sheet{left:115px;top:47px;width:977px;height:1050px;background:var(--white);border-radius:18px}
.header{left:115px;top:47px;width:977px;height:140px;border-radius:18px 18px 0 0;background:linear-gradient(180deg,#fafafa,#bdbdbd 75%,#e6e6e6)}
.brand{left:143px;top:62px;font-family:"PT Sans",sans-serif;font-weight:700;font-size:38px;color:#2f2f2f;line-height:1}
.brand small{display:block;font-size:22px;color:#2a7a4a;margin:6px 0 0 60px;font-weight:700}
.util{left:834px;top:66px;font-size:10px;color:#333;letter-spacing:.2px}
.util .rss{display:inline-block;width:20px;height:20px;background:#f39019;border-radius:3px;vertical-align:middle;margin-left:8px}
.nav a{position:absolute;top:99px;height:36px;border-radius:18px;background:linear-gradient(180deg,#4a4a4a,#151515);
  color:#fff;font-size:17px;font-weight:300;line-height:36px;text-align:center;text-decoration:none;border:1px solid #777}
.nav .on{background:linear-gradient(180deg,#b33cf5,#8a12cc);font-weight:700}
.band{left:0;top:168px;width:1200px;height:330px}
.photo{position:absolute;border:3px solid #fff}
.p1{left:154px;top:245px;width:230px;height:171px;background:linear-gradient(90deg,#dfe6ef,#8fb0d8 45%,#3a2a26)}
.p2{left:381px;top:197px;width:431px;height:263px;background:linear-gradient(90deg,#6a4a3a,#c99e86 35%,#b9d4ea 60%,#eef4fa)}
.p3{left:809px;top:249px;width:229px;height:166px;background:linear-gradient(90deg,#6b3e28,#c08a6d 40%,#d6e2ee)}
.box{position:absolute;width:288px;height:255px;background:var(--panel);border:1px solid #ddd}
.box .title{height:42px;border-radius:12px 12px 0 0;background:linear-gradient(180deg,#a52aea,#7a17b2);
  color:#fff;font-family:"PT Sans",sans-serif;font-style:italic;font-weight:700;font-size:21px;line-height:44px;text-align:center;margin:-1px -1px 0}
.box .inner{position:absolute;left:9px;right:9px;top:49px;bottom:8px}
.box .inner.white{background:#fff}
.c1{left:144px}.c2{left:459px}.c3{left:772px}
.r1{top:519px}.r2{top:796px}
.heading-link{font-family:"PT Sans",sans-serif;font-style:italic;font-weight:700;font-size:18px;text-decoration:underline;color:#111;line-height:22px}
.note{font-family:"PT Sans",sans-serif;font-style:italic;font-weight:700;color:var(--link);text-decoration:underline;font-size:15px;line-height:16px}
.body{font-size:14px;line-height:19px;font-weight:300;color:#222}
.body.tight{font-size:13.4px;letter-spacing:-.2px}
.vip{font-size:17px;line-height:23px;font-weight:300;color:#222}
.more{position:absolute;left:2px;bottom:0;font-family:"PT Sans",sans-serif;font-style:italic;font-weight:700;font-size:15px;color:var(--link)}
.more:before{content:"+ ";font-style:normal;color:#777}
.ph{position:absolute}
.dots{position:absolute;right:8px;bottom:2px;display:flex;gap:3px}
.dots i{width:18px;height:18px;border-radius:50%;border:2px solid var(--purple-dark);background:#fff}
.dots i.on{background:var(--purple-dark)}
.partner{font-family:"Open Sans",sans-serif;font-weight:700;color:#3a3a3a;position:absolute;left:2px}
.footer{left:120px;top:1112px;color:#fff;font-size:11.5px;font-weight:600;line-height:16px}
.social{left:553px;top:1124px;display:flex;gap:14px}
.social span{display:flex;align-items:center;gap:5px;color:#fff;font-size:11px;font-weight:600}
.social b{width:16px;height:16px;display:block;background:#fff}
.copy{right:108px;top:1127px;color:#fff;font-size:11.5px;font-weight:600}
</style>
</head>
<body>
<div class="topbar">
  <div class="pill cart">Your Chart is Empty, Currency: <b>???</b></div>
  <div class="pill checkout">Checkout Now</div>
  <div class="pill account">My Account <span class="arrow"></span></div>
</div>

<div class="abs sheet"></div>
<div class="abs header"></div>
<div class="abs brand">CORVELLE<small>&amp; Beauty</small></div>
<div class="abs util">SUPPORT &nbsp;|&nbsp; FAQS &nbsp;|&nbsp; SITEMAP &nbsp;|&nbsp; RRS FEED<span class="rss"></span></div>
<nav class="nav">
  <a class="on" href="#" style="left:408px;width:100px">Home</a>
  <a href="#" style="left:516px;width:100px">About us</a>
  <a href="#" style="left:620px;width:208px">Services &amp; Treatment</a>
  <a href="#" style="left:832px;width:102px">FAQ's</a>
  <a href="#" style="left:938px;width:122px">Contact us</a>
</nav>

<svg class="abs band" viewBox="0 0 1200 330" aria-hidden="true">
  <defs><linearGradient id="lens" x1="0" y1="0" x2="0" y2="1">
    <stop offset="0" stop-color="#d07af5"/><stop offset=".5" stop-color="#b13cf0"/><stop offset="1" stop-color="#9b1fe0"/></linearGradient></defs>
  <path d="M0 38 Q600 -30 1200 38 L1200 292 Q600 360 0 292 Z" fill="url(#lens)" stroke="#3a0f52" stroke-width="2"/>
</svg>
<div class="photo p1" role="img" aria-label="Skincare tubes and jars beside a smiling model"></div>
<div class="photo p3" role="img" aria-label="Model with long hair beside skincare bottles"></div>
<div class="photo p2" role="img" aria-label="Model resting on her hands with a collection of skincare products"></div>

<section class="box c1 r1">
  <div class="title">Introducting Our New Products</div>
  <div class="inner">
    <div class="heading-link">Range of Solenne Marine<br>Products</div>
    <div class="ph" role="img" aria-label="Solenne Marine tubes and jars" style="left:2px;top:60px;width:250px;height:140px;background:linear-gradient(90deg,#e8ecf2,#c8d4e6 50%,#4b6ea8)"></div>
    <div class="note abs" style="left:128px;top:44px;transform:rotate(10deg);text-align:center">Click here to see<br>full range of products</div>
  </div>
</section>

<section class="box c2 r1">
  <div class="title">Revolutionary new treatments</div>
  <div class="inner white" style="left:8px;right:8px">
    <div class="ph" role="img" aria-label="Treatment video still" style="left:0;top:0;width:270px;height:172px;background:linear-gradient(180deg,#222 0,#b8d7ea 12%,#5f8aa6 55%,#111)"></div>
    <svg class="ph" style="left:116px;top:73px" width="50" height="28"><rect width="50" height="28" rx="5" fill="#111" stroke="#888"/><path d="M19 7 L33 14 L19 21Z" fill="#fff"/></svg>
    <div class="ph" style="left:0;top:174px;width:270px;height:26px;background:#e3e3e3;border:1px solid #bbb;font-size:10px;line-height:24px;padding-left:78px">0:00 / 0:00 <span style="margin-left:60px;font-weight:700">Playhouse</span></div>
  </div>
</section>

<section class="box c3 r1">
  <div class="title">Our Products</div>
  <div class="inner">
    <div class="ph" style="left:-3px;top:-2px;width:290px;height:36px;background:#9c1c2a;border-radius:0 18px 18px 0;color:#fff;font-family:'PT Sans',sans-serif;font-weight:700;font-size:26px;line-height:36px;text-align:right;padding-right:18px">Fresh Dawn</div>
    <div class="ph" role="img" aria-label="Fresh Dawn cleanser bottle and tubes" style="left:10px;top:40px;width:140px;height:150px;background:linear-gradient(90deg,#f4f4f4,#e8e8e8 50%,#d9d9d9)"></div>
    <div class="note abs" style="left:190px;top:98px">For brief<br>Click here</div>
    <div class="dots"><i></i><i></i><i></i><i></i><i class="on"></i></div>
  </div>
</section>

<section class="box c1 r2">
  <div class="title">EXELLENCE IN SKIN CARE</div>
  <div class="inner">
    <div class="partner" style="top:4px;font-size:30px">Velmoracine</div>
    <div class="partner" style="top:74px;font-size:22px;color:#2f8a3a">Verdant Renewal Peel</div>
    <div class="partner" style="top:138px;font-size:26px;font-weight:400">Aurelis Circle</div>
    <div class="more">Read more</div>
  </div>
</section>

<section class="box c2 r2">
  <div class="title">Latest News</div>
  <div class="inner white">
    <div class="heading-link" style="margin-top:4px">Corvelle on the top ...</div>
    <p class="body" style="margin-top:16px;border-bottom:1px solid #555;padding-bottom:8px">Corvelle &amp; Beauty is a health, massage skincare centre that provides quality treatments and education to each and every client to cater for all individuals.</p>
    <p class="body" style="margin-top:8px">Corvelle &amp; Beauty is a health, massage skincare centre that provides quality....</p>
    <div class="more">Read more</div>
  </div>
</section>

<section class="box c3 r2">
  <div class="title">Contact Us</div>
  <div class="inner white">
    <div class="heading-link" style="margin-top:4px">Join us on Circlebook</div>
    <div class="ph" style="left:196px;top:4px;width:58px;height:58px;border-radius:8px;background:#3b5fa8"></div>
    <p class="body tight" style="margin-top:40px">Become a friend on Circlebook and be one of the first to receive all our latest news.</p>
    <p class="vip" style="margin-top:12px">Join our VIP club and earn discounts on products</p>
    <div class="more">Read more</div>
  </div>
</section>

<div class="abs footer">OUR LOCATION:<br>Unit 4 / 27 Marlow Road, ELMSFORD, WA 6021.<br><span style="display:block;margin-top:8px">Phone: (08) 9400 1234</span></div>
<div class="abs social"><span><b></b>Circlebook</span><span><b></b>Tumbleweave</span><span><b style="background:#f39019"></b>Feed</span></div>
<div class="abs copy">©2011 - Corvelle &amp; Beauty &nbsp;|&nbsp; All Rights Reserved</div>
</body>
</html>
```